Book Cover for Memoir: Sexual Assault and Traumatic Stress

I need a cover design for a memoir that is a victim's story of a sexual assault. I will need a print-on-demand cover, an eBook cover, and a 3D thumbnail image. The thumbnail and eBook cover will be used immediately, and the POD cover will be used in a few months with the full manuscript is ready. Therefore, I need an artist who is willing to make small adjustments if needed once the page count is set.

I have a image I have purchased that should give you an idea of the desired direction, but you can feel free to use your own images. I have attached some examples of book covers I like. I attached a color palette for fonts.

Overall Look: Fonts should be feminine and thin, but large to stand out. Look should be simple and elegant, and display and overall depressing feeling. There should be enough detail though to make it look professionally put together. Not TOO minimalistic.

I have also attached the Print Harbor templates if you choose to use those. If not, ensure there is an open place for the barcode on the bottom right.

Requirements
Must have
• Title: Beneath Quiet Rain
Subtitle: One Woman's Account of Fear, Guilt & Silence
Author: Dana Ruth Whitford
Audience: Mostly women 18-30
Quote (for the back): "I always thought I'd know how I'd react if I ever was raped. I was wrong. I've been wrong a lot lately."
Summary (back cover): When twenty-seven-year-old Dana Whitford wakes up with a gut-wrenching feeling, she has little memory of the horrifying events that occurred the night before. Days earlier, Dana was a spirited single mom who had abandoned her hometown to raise her daughter in the city and pursue her dreams. In the short months since Dana’s move to Seattle, she became the adored lover of a charismatic lawyer, started a new business, and finally felt life was going her way. So what happened to cause her to break?

In a gripping and heartbreaking narrative, Dana tells the true story of how her life unraveled from the traumatic events that took place that night and why what seems obvious to everyone else is impossible for Dana to believe. Beneath Quiet Rain is a chilling exploration of memory through trauma, trust in humanity, and a captivating story of strength and survival that appeals to the heart of fathers and mothers, sons and daughters, and men and women alike.
Nice to have
• BACK COVER: I'd like to have a photo on the back. This should depict the happy life of the main character before the sexual assault, and should be with her daughter. Or should be a nature scene that starts at the corner and blends into the rest of the cover. I have attached a possible image or you can use something you like.

```html
<!DOCTYPE html>
<html lang="en">
<head>
<meta charset="utf-8">
<title>Beneath Quiet Rain — Cover Spread</title>
<link rel="stylesheet" href="https://fonts.googleapis.com/css2?family=Ribeye&family=Almendra+SC&family=Raleway:wght@300&family=Open+Sans:wght@400&family=Crimson+Text:ital,wght@1,400;1,600&display=swap">
<style>
  :root {
    --back-bg: #766b5f;
    --title-pink: #e72b8c;
    --author-grey: #6f6a66;
    --subtitle-grey: #6e655e;
    --paper-white: #ffffff;
    --photo-light: #f1eeea;
    --photo-warm: #e3ddd5;
    --photo-shadow: #cfc7bd;
  }
  * { box-sizing: border-box; margin: 0; padding: 0; }
  html, body { width: 1200px; height: 842px; overflow: hidden; background: #ffffff; }
  .spread { position: relative; width: 1200px; height: 842px; overflow: hidden; }

  /* Back cover */
  .back-cover {
    position: absolute; left: 0; top: 0; width: 561px; height: 842px;
    background: var(--back-bg); color: var(--paper-white); overflow: hidden;
  }
  .back-quote {
    font-family: "Crimson Text", Georgia, serif; font-style: italic; font-weight: 600;
    color: var(--paper-white); position: absolute; left: 0; top: 0;
  }
  .back-quote .line { position: absolute; white-space: nowrap; }
  .back-quote .line-1 { left: 50px; top: 34px; font-size: 21px; letter-spacing: -0.2px; }
  .back-quote .line-2 { left: 91px; top: 70px; font-size: 24px; }
  .back-quote .line-3 { left: 212px; top: 104px; font-size: 23px; }
  .back-photo {
    position: absolute; left: 114px; top: 153px; width: 328px; height: 192px;
    background: linear-gradient(100deg, #5b4a42 0%, #b9aea3 30%, #eef0ee 55%, #d7d6d1 80%, #8e8a80 100%);
  }
  .back-blurb {
    position: absolute; left: 39px; top: 380px; width: 512px;
    font-family: "Open Sans", Arial, sans-serif; font-size: 12.6px; line-height: 17.4px;
  }
  .back-blurb p + p { margin-top: 17px; }
  .barcode-space {
    position: absolute; left: 357px; top: 688px; width: 186px; height: 140px;
    background: var(--paper-white);
  }

  /* Front cover & spine photo area */
  .cover-photo {
    position: absolute; left: 561px; top: 0; width: 639px; height: 842px;
    background:
      radial-gradient(ellipse 180px 330px at 330px 540px, var(--photo-shadow) 0%, rgba(207,199,189,0) 100%),
      linear-gradient(180deg, var(--photo-light) 0%, var(--photo-warm) 60%, #f4f3f1 78%, #fbfbfa 100%);
  }
  .spine-title, .spine-author {
    position: absolute; transform-origin: left top; transform: rotate(90deg); white-space: nowrap;
  }
  .spine-title {
    left: 612px; top: 40px; font-family: "Ribeye", cursive; font-size: 40px;
    color: var(--title-pink); letter-spacing: 1px;
  }
  .spine-author {
    left: 606px; top: 606px; font-family: "Raleway", Arial, sans-serif; font-weight: 300;
    font-size: 21px; color: var(--author-grey);
  }
  .front-title {
    position: absolute; left: 0; top: 0; font-family: "Ribeye", cursive; color: var(--title-pink);
    font-weight: 400; line-height: 1;
  }
  .front-title .word { position: absolute; white-space: nowrap; }
  .front-title .word-1 { left: 662px; top: 28px; font-size: 76px; }
  .front-title .word-2 { left: 730px; top: 152px; font-size: 112px; }
  .front-title .word-3 { left: 945px; top: 300px; font-size: 100px; }
  .front-subtitle {
    position: absolute; left: 995px; top: 36px; width: 195px;
    font-family: "Almendra SC", Georgia, serif; font-size: 15px; line-height: 20px;
    color: var(--subtitle-grey); text-align: center;
  }
  .front-author {
    position: absolute; left: 890px; top: 768px; width: 290px; text-align: right;
    font-family: "Raleway", Arial, sans-serif; font-weight: 300; font-size: 33px;
    color: var(--author-grey); white-space: nowrap;
  }
</style>
</head>
<body>
<main class="spread">
  <section class="back-cover">
    <blockquote class="back-quote">
      <span class="line line-1">"I always thought I'd know how I'd react if I ever was raped.</span>
      <span class="line line-2">I was wrong.</span>
      <span class="line line-3">I've been wrong a lot lately."</span>
    </blockquote>
    <div class="back-photo" role="img" aria-label="Photo of a smiling young mother and her small daughter by a bright window"></div>
    <div class="back-blurb">
      <p>When twenty-seven-year-old Dana Whitford wakes up with a gut-wrenching feeling, she has little memory of the horrifying events that occurred the night before. Days earlier, Dana was a spirited single mom who had abandoned her hometown to raise her daughter in the city and pursue her dreams. In the short months since Dana's move to Seattle, she became the adored lover of a charismatic lawyer, started a new business, and finally felt life was going her way. So what happened to cause her to break?</p>
      <p>In a gripping and heartbreaking narrative, Dana tells the true story of how her life unraveled from the traumatic events that took place that night and why what seems obvious to everyone else is impossible for Dana to believe. Beneath Quiet Rain is a chilling exploration of memory through trauma, trust in humanity, and a captivating story of strength and survival that appeals to the heart of fathers and mothers, sons and daughters, and men and women alike.</p>
    </div>
    <div class="barcode-space"></div>
  </section>

  <div class="cover-photo" role="img" aria-label="Photo of a young woman with long dark hair sitting curled on a white bed, head buried in her knees, against a pale wall"></div>

  <div class="spine-title">Beneath Quiet Rain</div>
  <div class="spine-author">Dana Ruth Whitford</div>

  <h1 class="front-title">
    <span class="word word-1">Beneath</span>
    <span class="word word-2">Quiet</span>
    <span class="word word-3">Rain</span>
  </h1>
  <p class="front-subtitle">One Woman's Account of Fear, Guilt &amp; Silence</p>
  <p class="front-author">Dana Ruth Whitford</p>
</main>
</body>
</html>
```